Copper Lantern Podcast Business Card Design

Needing a business card with the logo design provided for Copper Lantern Podcast. I am looking for a modern style that fits the current logo.

Info:
Name: Bao Khanh
Title: Creator/Host
Email: bao@copperlanternpod.com
Phone: (405) 637-2918
www.copperlanternpod.com
Twitter: @coplanternpod
Instagram: @copperlanternpodcast
Facebook: Copper Lantern Podcast

Industry/Entity Type

Business

Font styles to use
Sans Serif

Colors
000000
ffffff

Requirements
Must have
• modern, clean design
Nice to have
• social media contact info

```html
<!DOCTYPE html>
<html lang="en">
<head>
<meta charset="utf-8">
<title>Copper Lantern Podcast – Business Card</title>
<link rel="stylesheet" href="https://fonts.googleapis.com/css2?family=Lato:wght@400;700&display=swap">
<style>
  :root {
    --stage: #1c1c1c;
    --card-dark: #0d0d0d;
    --card-dark-edge: #262626;
    --card-light: #ffffff;
    --silver: #cfcfcf;
    --silver-soft: #9a9a9a;
    --ink: #1a1a1a;
    --mark-grey: #3a3a3e;
    --divider: #8a8a8a;
  }
  * { margin: 0; padding: 0; box-sizing: border-box; }
  html, body {
    width: 1200px; height: 1000px; overflow: hidden;
    background: var(--stage);
    font-family: "Lato", sans-serif;
  }
  .canvas { position: relative; width: 1200px; height: 1000px; }

  .card {
    position: absolute; left: 250px; width: 700px; height: 400px;
    box-shadow: 0 14px 30px rgba(0,0,0,.55);
  }

  /* Front */
  .card-front {
    top: 60px;
    background: linear-gradient(160deg, var(--card-dark-edge), var(--card-dark) 60%);
    display: flex; flex-direction: column; align-items: center; justify-content: center;
    gap: 26px;
  }
  .front-square {
    width: 110px; height: 110px; border: 3px solid var(--silver);
  }
  .front-wordmark {
    text-align: center; color: var(--silver); font-weight: 700;
    text-transform: uppercase; line-height: 1.1;
  }
  .front-wordmark .name-main { display: block; font-size: 46px; letter-spacing: 1px; }
  .front-wordmark .name-sub { display: block; font-size: 15px; letter-spacing: 12px; margin-top: 6px; }

  /* Back */
  .card-back {
    top: 540px; background: var(--card-light);
    display: flex; align-items: center;
  }
  .back-mark {
    width: 310px; padding-left: 50px;
    color: var(--mark-grey); font-weight: 700; font-size: 36px;
    text-transform: uppercase; line-height: 1.05; letter-spacing: 1px;
  }
  .back-divider {
    width: 2px; height: 250px;
    background: linear-gradient(to bottom, transparent, var(--divider) 30%, var(--divider) 70%, transparent);
    margin-right: 28px;
  }
  .contact { color: var(--ink); }
  .contact-name { font-weight: 700; font-size: 24px; letter-spacing: .5px; text-transform: uppercase; }
  .contact-title { font-size: 16px; color: #444; margin-bottom: 26px; }
  .contact-list { list-style: none; font-size: 16px; }
  .contact-list li { display: flex; align-items: center; gap: 10px; height: 24px; }
  .contact-list svg { width: 14px; height: 14px; flex: none; }
</style>
</head>
<body>
<main class="canvas">

  <section class="card card-front" aria-label="Card front">
    <div class="front-square"></div>
    <h1 class="front-wordmark">
      <span class="name-main">Copper Lantern</span>
      <span class="name-sub">Podcast</span>
    </h1>
  </section>

  <section class="card card-back" aria-label="Card back">
    <div class="back-mark">Copper<br>Lantern</div>
    <div class="back-divider"></div>
    <div class="contact">
      <h2 class="contact-name">Bao Khanh</h2>
      <p class="contact-title">Creator/Host</p>
      <ul class="contact-list">
        <li>
          <svg viewBox="0 0 14 14"><rect x="1" y="3" width="12" height="8" fill="none" stroke="#333" stroke-width="1.2"/><path d="M1 3l6 5 6-5" fill="none" stroke="#333" stroke-width="1.2"/></svg>
          bao@copperlanternpod.com
        </li>
        <li>
          <svg viewBox="0 0 14 14"><circle cx="7" cy="7" r="6" fill="none" stroke="#333" stroke-width="1.2"/><path d="M5 4l1 2-1 1 2 2 1-1 2 1-1 2c-3 0-6-3-6-6z" fill="#333"/></svg>
          (405) 637-2918
        </li>
        <li>
          <svg viewBox="0 0 14 14"><circle cx="7" cy="7" r="6" fill="none" stroke="#333" stroke-width="1.2"/><ellipse cx="7" cy="7" rx="2.5" ry="6" fill="none" stroke="#333" stroke-width="1"/><path d="M1 7h12" stroke="#333" stroke-width="1"/></svg>
          www.copperlanternpod.com
        </li>
        <li>
          <svg viewBox="0 0 14 14"><circle cx="7" cy="7" r="6" fill="none" stroke="#333" stroke-width="1.2"/></svg>
          @coplanternpod
        </li>
        <li>
          <svg viewBox="0 0 14 14"><circle cx="7" cy="7" r="6" fill="none" stroke="#333" stroke-width="1.2"/></svg>
          @copperlanternpodcast
        </li>
        <li>
          <svg viewBox="0 0 14 14"><circle cx="7" cy="7" r="6" fill="none" stroke="#333" stroke-width="1.2"/></svg>
          Copper Lantern Podcast
        </li>
      </ul>
    </div>
  </section>

</main>
</body>
</html>
```